New Menu for Elegant Cafe Pastry Shop

We need to choose a design and layout for our new menu. We would like to also condense our current menu to 4-6 pages.
We will be changing prices and items on the menu, so it needs to be editable. Adobe formats are preferred. The size of the pages needs to be letter size. We will be printing it in house
Please take inspiration from the photos of our shop and food and also our Picmosaic page.
Attached are our current menu our logo and the logo info

https://www.picmosaic.com/marbrecoquette/?hl=en
https://maps.wayfindr.app/Qk3Lm9Xp2Tb7VwR4a

Industry/Entity Type

Food Cafe Bakery pastry

Other font styles liked:
• please look at attached files

Colors

Designer to choose colors to be used in the design.

Requirements
Nice to have
• Use of Arches like on our shop wallpaper or oblong eclair shapes, Art Deco elements

```html
<!DOCTYPE html>
<html lang="en">
<head>
<meta charset="utf-8">
<title>Marbre Coquette — Menu</title>
<link href="https://fonts.googleapis.com/css2?family=Italiana&family=Oswald:wght@500&family=Poppins:wght@300;400&display=swap" rel="stylesheet">
<style>
:root{
  --teal:#45c0c9;
  --teal-soft:#8fdbe0;
  --backdrop:#000;
  --paper:#fff;
  --ink:#2b2030;
  --rule:#4a3550;
  --nuts:#1d3f8f;
  --gf:#d0302a;
  --vegan:#2f8f3a;
}
*{margin:0;padding:0;box-sizing:border-box}
html,body{width:1200px;height:2320px;overflow:hidden;background:var(--backdrop)}
.canvas{position:relative;width:1200px;height:2320px}
.page{position:absolute;left:184px;width:832px;background:var(--paper);overflow:hidden}
.page--seasonal{top:61px;height:1076px}
.page--drinks{top:1179px;height:1076px}
.abs{position:absolute}
.teal-field{position:absolute;left:0;top:0}
.brand{position:absolute;left:56px;top:196px;width:270px;text-align:center;font-family:'Italiana',serif;font-size:38px;letter-spacing:2px;color:var(--teal);line-height:1.1}
.brand-dot{position:absolute;left:176px;top:136px;width:30px;height:30px;border-radius:50%;background:var(--teal)}
.display{font-family:'Italiana',serif;font-weight:400;line-height:1}
.label{font-family:'Oswald',sans-serif;font-weight:500;text-transform:uppercase;letter-spacing:.5px}
.body{font-family:'Poppins',sans-serif;font-weight:300}
.on-teal{color:var(--paper)}
.row{position:absolute;display:flex;justify-content:space-between;font-family:'Oswald',sans-serif;font-weight:500;text-transform:uppercase}
.page--seasonal .row{left:439px;width:321px;font-size:17px;color:var(--paper)}
.divider{position:absolute}
.scroll-mark{position:absolute;background:var(--rule);border-radius:50%}
.ornament{position:absolute}
.legend{position:absolute;left:0;width:832px;top:983px;text-align:center;font-family:'Oswald',sans-serif;font-weight:500;font-size:11.5px;color:var(--ink)}
.legend b{font-weight:500;color:var(--nuts)}
.legend .gf{color:var(--gf)}
.legend .v{color:var(--vegan)}
.band{position:absolute;left:214px;width:404px;background:var(--teal);color:var(--paper);text-align:center;font-family:'Italiana',serif}
.col-title{position:absolute;font-family:'Italiana',serif;font-weight:400;font-size:28px;color:var(--ink);top:0;line-height:1}
.desc{position:absolute;font-family:'Poppins',sans-serif;font-weight:300;font-size:12.5px;line-height:16.5px;color:var(--ink);letter-spacing:.4px}
.page--drinks .row{font-size:11px;color:var(--ink);height:24px}
.syrups{position:absolute;left:0;width:832px;top:631px;text-align:center;font-family:'Poppins',sans-serif;font-weight:300;font-size:13.5px;line-height:18px;color:var(--ink);letter-spacing:.6px}
.vsep{position:absolute;width:14px}
</style>
</head>
<body>
<div class="canvas">

  <section class="page page--seasonal">
    <svg class="teal-field" width="832" height="1076" viewBox="0 0 666 861" aria-hidden="true">
      <path d="M393 0 L666 0 L666 650 Q666 766 550 766 L80 766 Q3 766 3 680 Q3 420 110 290 A140 140 0 0 0 283 111 Q320 30 393 0 Z" fill="var(--teal)"/>
    </svg>

    <div class="brand-dot"></div>
    <div class="brand">MARBRE<br>COQUETTE</div>

    <h1 class="abs display on-teal" style="left:439px;top:160px;font-size:68px">Seasonal</h1>
    <p class="abs body on-teal" style="left:635px;top:223px;font-size:13px;letter-spacing:1px">Upon availability</p>

    <h2 class="abs display on-teal" style="left:512px;top:314px;width:200px;text-align:center;font-size:42px">Soups</h2>
    <div class="row" style="top:381px;left:461px;width:299px"><span>Lorraine</span><span>|&nbsp; $6.99</span></div>

    <svg class="divider" style="left:487px;top:432px" width="250" height="16" viewBox="0 0 250 16" aria-hidden="true">
      <path d="M3 13 Q2 8 7 8 L243 8 Q248 8 247 13" stroke="var(--rule)" stroke-width="1.6" fill="none"/>
    </svg>
    <div class="scroll-mark" role="img" aria-label="Small scroll ornament" style="left:596px;top:433px;width:32px;height:12px"></div>

    <h2 class="abs display on-teal" style="left:438px;top:482px;width:300px;text-align:center;font-size:44px">Travel Cakes V</h2>
    <div class="row" style="top:559px"><span>Banana Pecan CN</span><span>$6.00</span></div>
    <div class="row" style="top:596px"><span>Banana Walnut CN</span><span>$6.00</span></div>
    <div class="row" style="top:634px"><span>Banana Chocolate Chips</span><span>$6.00</span></div>
    <div class="row" style="top:671px"><span>Blueberry</span><span>$6.00</span></div>

    <svg class="divider" style="left:487px;top:738px" width="250" height="16" viewBox="0 0 250 16" aria-hidden="true">
      <path d="M3 13 Q2 8 7 8 L243 8 Q248 8 247 13" stroke="var(--rule)" stroke-width="1.6" fill="none"/>
    </svg>
    <div class="scroll-mark" role="img" aria-label="Small scroll ornament" style="left:596px;top:739px;width:32px;height:12px"></div>

    <h2 class="abs display on-teal" style="left:438px;top:786px;width:300px;text-align:center;font-size:44px">Baba Au Rhum</h2>
    <p class="abs label on-teal" style="left:642px;top:826px;font-size:11px">Contain alcohol</p>
    <div class="row" style="top:866px"><span>Chocolate / Hazelnut Spread</span><span>$7.80</span></div>
    <div class="row" style="top:904px"><span>Vanilla/Orange/Pineapple</span><span>$7.80</span></div>

    <p class="abs label on-teal" style="left:81px;top:669px;font-size:17px">Pistachio Raspberry Opera CN &nbsp;| $ 8.80</p>
    <p class="abs body on-teal" style="left:81px;top:702px;font-size:13.5px;line-height:19px;letter-spacing:.5px">Pistachio joconde cake layered with<br>pistachio buttercream, chocolate<br>ganache and raspberry gelée.</p>

    <div class="ornament" role="img" aria-label="Teal flourish ornament, bottom left corner" style="left:31px;top:970px;width:100px;height:82px;background:linear-gradient(45deg,var(--teal),var(--teal-soft));border-radius:0 80% 0 0"></div>
    <div class="ornament" role="img" aria-label="Teal flourish ornament, bottom right corner" style="left:701px;top:970px;width:100px;height:82px;background:linear-gradient(315deg,var(--teal),var(--teal-soft));border-radius:80% 0 0 0"></div>

    <p class="legend"><b>(CN)</b> - CONTAINS NUTS <b>(CA)</b> - CONTAINS ALMONDS <b>(CW)</b> - CONTAINS WALNUTS <b class="gf">(GF)</b> - GLUTEN FREE <b class="v">(V)</b> - VEGAN</p>
  </section>

  <section class="page page--drinks">
    <div class="band" style="top:0;height:122px;font-size:60px;line-height:1;padding-top:52px">Mocktails</div>

    <div class="abs" style="left:0;top:162px;width:832px">
      <h3 class="col-title" style="left:75px">Pina Colada</h3>
      <p class="desc" style="left:75px;top:38px">A tropical classic mocktail<br>of pineapple and coconut<br>$ 6.30</p>
      <h3 class="col-title" style="left:320px">Mango Lychee</h3>
      <p class="desc" style="left:320px;top:34px">Refreshing mix of lychee and<br>mango<br>$ 6.50</p>
      <h3 class="col-title" style="left:591px">Shirley Temple</h3>
      <p class="desc" style="left:591px;top:38px">Ginger ale and grenadine<br>mocktail garnished with<br>maraschino cherry.<br>$ 6.30</p>
    </div>
    <svg class="vsep" style="left:278px;top:134px" width="14" height="128" viewBox="0 0 14 128" aria-hidden="true"><path d="M4 2 Q8 2 8 6 L8 122 Q8 126 4 126" stroke="var(--rule)" stroke-width="1.4" fill="none"/></svg>
    <div class="scroll-mark" role="img" aria-label="Small scroll ornament" style="left:282px;top:186px;width:9px;height:24px"></div>
    <svg class="vsep" style="left:538px;top:134px" width="14" height="128" viewBox="0 0 14 128" aria-hidden="true"><path d="M4 2 Q8 2 8 6 L8 122 Q8 126 4 126" stroke="var(--rule)" stroke-width="1.4" fill="none"/></svg>
    <div class="scroll-mark" role="img" aria-label="Small scroll ornament" style="left:542px;top:186px;width:9px;height:24px"></div>

    <div class="band" style="top:275px;height:50px;font-size:32px;line-height:50px">Coffees &amp; Beverages</div>

    <h3 class="col-title" style="left:75px;top:358px">Iced Coffee</h3>
    <div class="row" style="left:78px;width:152px;top:411px"><span>Iced Espresso</span><span>$4.00</span></div>
    <div class="row" style="left:78px;width:152px;top:435px"><span>Iced Cappuccino</span><span>$4.55</span></div>
    <div class="row" style="left:78px;width:152px;top:459px"><span>Iced Latte</span><span>$4.75</span></div>

    <h3 class="col-title" style="left:320px;top:358px">Hot Coffee</h3>
    <div class="row" style="left:320px;width:177px;top:407px"><span>Filter Coffee</span><span>$2.40</span></div>
    <div class="row" style="left:320px;width:177px;top:431px"><span>Espresso</span><span>$2.75</span></div>
    <div class="row" style="left:320px;width:177px;top:455px"><span>Cappuccino</span><span>$3.50</span></div>
    <div class="row" style="left:320px;width:177px;top:480px"><span>Latte</span><span>$3.70</span></div>
    <div class="row" style="left:320px;width:177px;top:504px"><span>Americano</span><span>$3.00</span></div>
    <div class="row" style="left:320px;width:177px;top:528px"><span>Espresso Macchiato</span><span>$3.00</span></div>

    <h3 class="col-title" style="left:591px;top:358px">Matcha</h3>
    <div class="row" style="left:591px;width:149px;top:411px"><span>Matcha Tea</span><span>$3.20</span></div>
    <div class="row" style="left:591px;width:149px;top:435px"><span>Matcha Latte Hot</span><span>$3.95</span></div>
    <div class="row" style="left:591px;width:149px;top:459px"><span>Matcha Latte Cold</span><span>$3.95</span></div>

    <svg class="vsep" style="left:268px;top:361px" width="14" height="173" viewBox="0 0 14 173" aria-hidden="true"><path d="M4 2 Q8 2 8 6 L8 167 Q8 171 4 171" stroke="var(--rule)" stroke-width="1.4" fill="none"/></svg>
    <div class="scroll-mark" role="img" aria-label="Small scroll ornament" style="left:272px;top:435px;width:9px;height:24px"></div>
    <svg class="vsep" style="left:542px;top:361px" width="14" height="173" viewBox="0 0 14 173" aria-hidden="true"><path d="M4 2 Q8 2 8 6 L8 167 Q8 171 4 171" stroke="var(--rule)" stroke-width="1.4" fill="none"/></svg>
    <div class="scroll-mark" role="img" aria-label="Small scroll ornament" style="left:546px;top:435px;width:9px;height:24px"></div>

    <div class="band" style="top:569px;height:46px;font-size:28px;line-height:46px">Syrups - Sauces - Toppings</div>
    <p class="syrups">vanilla | hazelnut | caramel | mocha | lavender | almond (ask for our sugar free options) +$1.00<br>dark or white chocolate sauce+$1.00 extra shot +$1.00 Decaf +$1.00</p>

    <h3 class="col-title" style="left:75px;top:717px">Cold Drinks</h3>
    <div class="row" style="left:75px;width:161px;top:757px"><span>Isle Spring Water 16 oz</span><span>$3.70</span></div>
    <div class="row" style="left:75px;width:161px;top:781px"><span>San Vitale</span><span>$4.70</span></div>
    <div class="row" style="left:75px;width:161px;top:806px"><span>Cola Classic / Diet</span><span>$4.00</span></div>
    <div class="row" style="left:75px;width:161px;top:830px"><span>Source Pétillante</span><span>$4.70</span></div>
    <div class="row" style="left:75px;width:161px;top:880px"><span>Homemade Lemonade</span><span>$6.50</span></div>
    <div class="row" style="left:75px;width:161px;top:904px"><span>Mint Lemonade</span><span>$6.50</span></div>
    <div class="row" style="left:75px;width:161px;top:928px"><span>Strawberry Lemonade</span><span>$6.50</span></div>
    <div class="row" style="left:75px;width:161px;top:953px"><span>Lavender Lemonade</span><span>$6.50</span></div>
    <div class="row" style="left:75px;width:161px;top:977px"><span>Orange Juice</span><span>$4.70</span></div>

    <h3 class="col-title" style="left:320px;top:717px">Tea</h3>
    <div class="row" style="left:320px;width:188px;top:757px"><span>Earl Grey</span><span>$3.50</span></div>
    <div class="row" style="left:320px;width:188px;top:781px"><span>Darjeeling</span><span>$3.50</span></div>
    <div class="row" style="left:320px;width:188px;top:806px"><span>Ginger Lemongrass</span><span>$3.50</span></div>
    <div class="row" style="left:320px;width:188px;top:830px"><span>Camomile</span><span>$3.50</span></div>
    <div class="row" style="left:320px;width:188px;top:855px"><span>Mint Vervain &amp; Herbs</span><span>$3.50</span></div>
    <div class="row" style="left:320px;width:188px;top:880px"><span>Fruit Symphony</span><span>$3.50</span></div>
    <div class="row" style="left:320px;width:188px;top:904px"><span>Dragon Sencha Green Tea</span><span>$3.50</span></div>
    <div class="row" style="left:320px;width:188px;top:928px"><span>Iced Tea</span><span>$3.50</span></div>

    <h3 class="col-title" style="left:591px;top:717px">Chocolate</h3>
    <div class="row" style="left:592px;width:131px;top:757px"><span>Chocolate Hot</span><span>$4.95</span></div>
    <div class="row" style="left:592px;width:131px;top:781px"><span>Chocolate Cold</span><span>$4.95</span></div>
    <div class="row" style="left:592px;width:131px;top:806px"><span>Whipped Cream</span><span>+$1.00</span></div>

    <svg class="vsep" style="left:266px;top:759px" width="14" height="203" viewBox="0 0 14 203" aria-hidden="true"><path d="M4 2 Q8 2 8 6 L8 197 Q8 201 4 201" stroke="var(--rule)" stroke-width="1.4" fill="none"/></svg>
    <div class="scroll-mark" role="img" aria-label="Small scroll ornament" style="left:270px;top:848px;width:9px;height:24px"></div>
    <svg class="vsep" style="left:547px;top:759px" width="14" height="203" viewBox="0 0 14 203" aria-hidden="true"><path d="M4 2 Q8 2 8 6 L8 197 Q8 201 4 201" stroke="var(--rule)" stroke-width="1.4" fill="none"/></svg>
    <div class="scroll-mark" role="img" aria-label="Small scroll ornament" style="left:551px;top:848px;width:9px;height:24px"></div>
  </section>

</div>
</body>
</html>
```